GLS biz card

We need a business card design for our new company based in Los Angeles called "Gold Lantern Studios". We develop film and television projects. We work with investors, financiers, film production companies, film distribution and sales companies as well as studios. We would like to incorporate our logo (see attached) on a two-sided card. We need to include: name and title, address, phone, email and company website.

Target Market(s)

Business, financial and studio clients

Industry/Entity Type

Business

Contact Information for Business Card

Two-sided. We are thinking of the logo on one side and the information on the back. Please feel free to be creative! Thanks.

Requirements
Must have
• Please include the following text information, excluding the "CAPS CATEGORY:" and please allow the ability for us to change the name, title and email address for each company employee):
• NAME & TITLE:
• Peter Harlow
• Managing Partner
• COMPANY NAME:
• GOLD LANTERN STUDIOS (please use existing logo)
• COMPANY ADDRESS:
• TKV Media Campus
• 2840 Welwood Avenue
• Tarlow Center, 4th Floor
• Westmere Bay, LV 90271
• COMPANY PHONE NUMBER:
• 555-555-0148
• COMPANY WEBSITE ADDRESS:
• www.goldlanternstudiosgroup.example
• EMAIL ADDRESS: (only one per card)
• martin@goldlanternstudiosgroup.example
• buzzy@goldlanternstudiosgroup.example
• peter@goldlanternstudiosgroup.example

```html
<!DOCTYPE html>
<html lang="en">
<head>
<meta charset="utf-8">
<title>Gold Lantern Studios – Business Card</title>
<link rel="stylesheet" href="https://fonts.googleapis.com/css2?family=Play:wght@400;700&display=swap">
<style>
  :root {
    --backdrop: #ebebeb;
    --card-light: #ffffff;
    --card-dark: #231f20;
    --logo-panel: #000000;
    --brand-cyan: #1ab3e6;
    --brand-disc: #0e6f8e;
    --ink-strong: #1a1a1a;
    --ink-soft: #444444;
    --shadow: rgba(0, 0, 0, 0.55);
  }
  * { margin: 0; padding: 0; box-sizing: border-box; }
  html, body {
    width: 1200px;
    height: 1000px;
    overflow: hidden;
    background: var(--backdrop);
    font-family: "Play", sans-serif;
  }
  .stage { position: relative; width: 1200px; height: 1000px; }

  .card {
    position: absolute;
    left: 333px;
    width: 548px;
    height: 320px;
    box-shadow: 4px 4px 4px var(--shadow);
  }
  .card--front { top: 157px; background: var(--card-light); }
  .card--back { top: 515px; height: 322px; background: var(--card-dark); }

  /* Front: logo tab */
  .logo-tab {
    position: absolute;
    left: 29px;
    top: -2px;
    width: 148px;
    height: 206px;
    background: var(--logo-panel);
  }
  .logo-tab .brand-disc {
    position: absolute;
    left: 37px;
    top: 76px;
    width: 74px;
    height: 74px;
    border-radius: 50%;
    background: var(--brand-disc);
  }
  .logo-tab .brand-name {
    position: absolute;
    left: 0;
    top: 157px;
    width: 148px;
    text-align: center;
    color: var(--brand-cyan);
    font-weight: 700;
    font-size: 10.5px;
    letter-spacing: 0.4px;
    white-space: nowrap;
  }

  /* Front: contact block */
  .contact {
    position: absolute;
    right: 28px;
    top: 54px;
    text-align: right;
    white-space: nowrap;
  }
  .contact .person-name { font-weight: 700; font-size: 19px; line-height: 22px; color: var(--ink-soft); }
  .contact .person-title { font-weight: 700; font-size: 16px; line-height: 20px; color: var(--ink-soft); }
  .contact .person-email { font-size: 16px; line-height: 22px; color: var(--ink-soft); }
  .contact .campus { margin-top: 16px; font-weight: 700; font-size: 16px; line-height: 20px; color: var(--ink-strong); }
  .contact .address-line { font-size: 14px; line-height: 17.5px; color: var(--ink-strong); }
  .contact .website { margin-top: 36px; font-size: 16px; line-height: 20px; color: var(--ink-strong); }

  /* Back: logo lockup */
  .card--back .brand-disc {
    position: absolute;
    left: 201px;
    top: 58px;
    width: 134px;
    height: 134px;
    border-radius: 50%;
    background: var(--brand-disc);
  }
  .card--back .brand-name {
    position: absolute;
    left: 0;
    top: 200px;
    width: 548px;
    text-align: center;
    color: var(--brand-cyan);
    font-weight: 700;
    font-size: 22px;
    letter-spacing: 1.5px;
    white-space: nowrap;
  }
</style>
</head>
<body>
<main class="stage">
  <section class="card card--front" aria-label="Card front">
    <div class="logo-tab">
      <div class="brand-disc"></div>
      <div class="brand-name">GOLD LANTERN STUDIOS</div>
    </div>
    <div class="contact">
      <p class="person-name">Peter Harlow</p>
      <p class="person-title">Director</p>
      <p class="person-email">peter@goldlanternstudiosgroup.example</p>
      <p class="campus">TKV Media Campus</p>
      <p class="address-line">2840 Welwood Avenue</p>
      <p class="address-line">Tarlow Center, 4th Floor</p>
      <p class="address-line">Westmere Bay, LV 90271</p>
      <p class="address-line">Phone: 555-555-0148</p>
      <p class="website">www.goldlanternstudiosgroup.example</p>
    </div>
  </section>

  <section class="card card--back" aria-label="Card back">
    <div class="brand-disc"></div>
    <div class="brand-name">GOLD LANTERN STUDIOS</div>
  </section>
</main>
</body>
</html>
```